Packaging Label Graphic Design

This design is for new packaging that we are about to launch. This label will go around our food container. We are hoping to go with some parts of the label clear (so you can still see the food inside) and the other half colored. We are open to your creativity. I will attached our logo , as that will need to be on there. As well as our website www.harvobrightfare.com, as well as instagram @harvobrightfare. We use the slogan "Elevate Your Life". You can use that too.
Our food is a healthier concept, and our food has a high volume of fresh ingredients. These containers will particularly be used for our Meal Prep(Fully cooked meals that you just need to heat up). The final design should look so goo that you would want to put it on your instagram before eating it :) The colours we currently play around with are navy blue, the grey and green you see in our logo, we also have a mustard colour that we have been implementing. Sizes that it needs to be is attached.

Target Market(s)

Ages 25-35

Requirements
Must have
• Our logo, website, & social media handles, a clear patch (with a design in it) so customers can see the food better. Get Creative.
Nice to have
• Color , stand out to customers, distinguished look.

```html
<!DOCTYPE html>
<html lang="en">
<head>
<meta charset="utf-8">
<title>Harvobright Meal Prep Label – Dieline</title>
<link rel="stylesheet" href="https://fonts.googleapis.com/css2?family=Arimo:wght@400;700&family=Montserrat:wght@800&display=swap">
<style>
  :root {
    --paper: #ffffff;
    --brand-green: #a3bd47;
    --brand-grey: #939393;
    --text-grey: #8a8a8a;
    --pattern-tint: #eef3dc;
    --dieline: #c2307f;
    --dimension: #9a9a9a;
  }
  html, body {
    margin: 0;
    padding: 0;
    width: 1200px;
    height: 524px;
    overflow: hidden;
    background: var(--paper);
  }
  .label-sheet { display: block; width: 1200px; height: 524px; }
  .dimension-line { stroke: var(--dimension); stroke-width: 1; fill: none; }
  .dimension-text { font-family: "Arimo", sans-serif; font-size: 13px; fill: var(--dimension); }
  .veg-pattern { fill: var(--pattern-tint); }
  .trim-line { fill: none; stroke: var(--dieline); stroke-width: 1.5; }
  .perf-line { stroke: var(--dieline); stroke-width: 1.5; stroke-dasharray: 6 4; }
  .perf-text { font-family: "Arimo", sans-serif; font-size: 13px; fill: var(--dieline); }
  .brand-panel { fill: var(--paper); stroke: var(--brand-green); stroke-width: 5; }
  .brand-name { font-family: "Montserrat", sans-serif; font-weight: 800; font-size: 66px; fill: var(--brand-grey); letter-spacing: 1px; }
  .brand-tagline { font-family: "Arimo", sans-serif; font-weight: 700; font-size: 35px; fill: var(--brand-green); }
  .tagline-divider { stroke: var(--brand-grey); stroke-width: 2.5; }
  .brand-web { font-family: "Arimo", sans-serif; font-size: 14px; fill: var(--text-grey); letter-spacing: 2px; }
  .brand-social { font-family: "Arimo", sans-serif; font-size: 12.5px; fill: var(--brand-green); letter-spacing: 1px; }
  .social-dot { fill: var(--brand-grey); }
</style>
</head>
<body>
<svg class="label-sheet" viewBox="0 0 1200 524" xmlns="http://www.w3.org/2000/svg">
  <!-- overall width -->
  <g class="dim-width">
    <line class="dimension-line" x1="53" y1="18" x2="1183" y2="18"/>
    <line class="dimension-line" x1="53" y1="10" x2="53" y2="26"/>
    <line class="dimension-line" x1="1183" y1="10" x2="1183" y2="26"/>
    <text class="dimension-text" x="617" y="11" text-anchor="middle">10.875″</text>
  </g>

  <!-- overall height -->
  <g class="dim-height">
    <line class="dimension-line" x1="26" y1="50" x2="26" y2="466"/>
    <line class="dimension-line" x1="18" y1="50" x2="35" y2="50"/>
    <line class="dimension-line" x1="18" y1="466" x2="35" y2="466"/>
    <text class="dimension-text" x="7" y="247" text-anchor="middle">4″</text>
  </g>

  <!-- vegetable line pattern area -->
  <rect class="veg-pattern" x="36" y="35" width="1164" height="446" role="img" aria-label="Repeating pattern of green outlined vegetables: broccoli, carrots, eggplants, beets and tomatoes"/>

  <!-- trim and perforation -->
  <rect class="trim-line" x="53" y="50" width="1130" height="416" rx="12"/>
  <line class="perf-line" x1="286" y1="50" x2="286" y2="466"/>
  <text class="perf-text" x="286" y="499" text-anchor="middle">PERF</text>

  <!-- clear window width -->
  <g class="dim-window">
    <line class="dimension-line" x1="53" y1="516" x2="286" y2="516"/>
    <line class="dimension-line" x1="53" y1="508" x2="53" y2="524"/>
    <line class="dimension-line" x1="286" y1="508" x2="286" y2="524"/>
    <text class="dimension-text" x="169" y="510" text-anchor="middle">2.25″</text>
  </g>

  <!-- brand panel -->
  <g class="brand-block">
    <rect class="brand-panel" x="428" y="143" width="622" height="227" rx="14"/>
    <text class="brand-name" x="744" y="260" text-anchor="middle" textLength="520" lengthAdjust="spacingAndGlyphs">HARVOBRIGHT</text>
    <text class="brand-tagline" x="481" y="301" textLength="296" lengthAdjust="spacingAndGlyphs">HEALTHY KITCHEN</text>
    <line class="tagline-divider" x1="800" y1="272" x2="800" y2="305"/>
    <text class="brand-tagline" x="821" y="301" textLength="185" lengthAdjust="spacingAndGlyphs">MEAL PREP</text>
    <text class="brand-web" x="735" y="329" text-anchor="middle">www.harvobrightfare.com</text>
    <text class="brand-social" x="997" y="350" text-anchor="end">@harvobrightfare</text>
    <circle class="social-dot" cx="1014" cy="345" r="11"/>
  </g>
</svg>
</body>
</html>
```